Dentistry on Marlow Marketing Brochure

I require a brochure to market our practice and to send to new patients after they have made initial phone contact, in our 'new patient package' .
My preference is for a double sided A4 trifold brochure.
Please find attached the style guide and information to be included.
Also, please visit our website at www.dentistryonmarlow.com.au to get an idea of our brand- we prefer a clean, fresh look that still conveys warmth and professionalism.
The images from our website can be used for the brochure.
Please include the map attached.

```html
<!DOCTYPE html>
<html lang="en">
<head>
<meta charset="utf-8">
<title>Dentistry on Marlow – Brochure</title>
<link rel="stylesheet" href="https://fonts.googleapis.com/css2?family=Crimson+Text:ital@1&family=PT+Sans:wght@400&display=swap">
<style>
  :root {
    --panel-grey: #e7e7e8;
    --text-grey: #6d6e71;
    --lime: #a7b51f;
    --white: #ffffff;
    --map-bg: #f1f1ee;
    --serif: "Crimson Text", Georgia, serif;
    --sans: "PT Sans", Arial, sans-serif;
  }
  * { margin: 0; padding: 0; box-sizing: border-box; }
  html, body { width: 1200px; height: 848px; overflow: hidden; background: var(--white); }
  .brochure { position: relative; width: 1200px; height: 848px; font-family: var(--sans); color: var(--text-grey); }
  .panel { position: absolute; top: 0; height: 848px; }
  .panel--hygiene { left: 0; width: 400px; background: var(--panel-grey); }
  .panel--info { left: 400px; width: 400px; background: var(--white); }
  .panel--cover { left: 800px; width: 400px; background: var(--white); }

  .heading { font-family: var(--serif); font-style: italic; font-weight: 400; color: var(--lime); font-size: 26px; letter-spacing: 0.6px; line-height: 1; margin-bottom: 9px; }
  .body-copy { font-size: 15px; line-height: 18.9px; }
  .body-copy p + p { margin-top: 18.9px; }

  .hygiene-text { position: absolute; left: 61px; top: 62px; width: 312px; }

  .photo { position: absolute; overflow: hidden; }
  .photo--hygienist { left: 0; top: 648px; width: 400px; height: 200px; border-top-right-radius: 36px;
    background: linear-gradient(100deg, #d9d4cf 0%, #ece8e4 45%, #c7b7ac 80%, #9c8a80 100%); }

  .info-block { position: absolute; left: 432px; width: 350px; }
  .payments { top: 62px; }
  .payment-list { list-style: none; font-size: 15px; line-height: 18.8px; }
  .payment-list li::before { content: "•"; margin-right: 6px; }
  .payment-note { font-style: italic; font-size: 15px; line-height: 21px; }

  .contact { top: 250px; }
  .contact-table { font-size: 15px; line-height: 19.5px; border-collapse: collapse; }
  .contact-table th { font-weight: 400; text-align: left; padding-right: 14px; }
  .social { top: 362px; font-family: var(--serif); font-style: italic; font-size: 30px; letter-spacing: 0.6px; color: var(--text-grey); }

  .hours { top: 412px; }
  .hours-table { font-size: 15px; line-height: 19px; border-collapse: collapse; }
  .hours-table th { font-weight: 400; text-align: left; width: 154px; }
  .urgent { top: 497px; font-size: 15px; }
  .parking { top: 535px; width: 140px; font-size: 15px; line-height: 19px; }
  .map { position: absolute; left: 600px; top: 550px; width: 126px; height: 236px; background: var(--map-bg); }

  .brand { position: absolute; left: 820px; top: 86px; width: 314px; text-align: right; }
  .brand-name { font-family: var(--sans); font-size: 38px; color: var(--text-grey); line-height: 1; white-space: nowrap; }
  .brand-tagline { font-family: var(--serif); font-style: italic; font-size: 15px; letter-spacing: 2.4px; margin-top: 10px; white-space: nowrap; }

  .photo--exterior { left: 800px; top: 222px; width: 400px; height: 142px; border-top-left-radius: 38px;
    background: linear-gradient(180deg, #e9e5df 0%, #d6cdc1 60%, #9aa07a 100%); }
  .photo--reception { left: 800px; top: 366px; width: 400px; height: 254px; border-top-left-radius: 38px;
    background: linear-gradient(100deg, #e6e2dd 0%, #55524f 30%, #dcd6ce 55%, #d9785c 85%, #cf5a3c 100%); }
  .photo--smile { left: 800px; top: 622px; width: 400px; height: 226px; border-top-left-radius: 38px;
    background: linear-gradient(100deg, #ded8d2 0%, #c9b0a0 40%, #e2d8cf 60%, #9c8d9b 100%); }
</style>
</head>
<body>
<main class="brochure">
  <section class="panel panel--hygiene"></section>
  <section class="panel panel--info"></section>
  <section class="panel panel--cover"></section>

  <article class="hygiene-text">
    <h2 class="heading">Hygiene Maintenance</h2>
    <div class="body-copy">
      <p>We have a strong focus on regular hygiene maintenance for all our patients and believe prevention of dental disease is smarter and more economical than treatment. There is a growing body of evidence highlighting the relationship between oral disease and systemic diseases such as cardiovascular disease, diabetes, arthritis and sleep apnoea. Emerging evidence suggests that improving oral health can actually lower your risk of some systemic diseases. We believe this increases the importance of maintaining optimum oral health, as it’s not just for your teeth and gums, but for the benefit of your whole body.</p>
      <p>Your hygiene maintenance appointments are performed by a hygienist, practitioners who are qualified specifically in the prevention of dental disease. To save you time, these appointments are typically combined with your dental examination.<br>Most people require a hygiene appointment every six months to maintain optimal oral health, however your hygienist will assess how often you should attend based on your needs. People with certain dental and health conditions may need to attend more frequently. As well as the benefits to your mouth and your body, your teeth will feel fantastic!</p>
    </div>
  </article>
  <div class="photo photo--hygienist" role="img" aria-label="Photo of a hygienist showing a smiling patient a dental model in the surgery"></div>

  <section class="info-block payments">
    <h2 class="heading">Payment options</h2>
    <ul class="payment-list">
      <li>Electronic Healthclaim facilities available</li>
      <li>DebitPay</li>
      <li>All major credit cards</li>
      <li>Cash</li>
      <li>Cheque</li>
    </ul>
    <p class="payment-note">Finance options available<br>DVA patients welcome, CDBS patients welcome</p>
  </section>

  <section class="info-block contact">
    <h2 class="heading">Contact Us</h2>
    <table class="contact-table">
      <tr><th>Phone:</th><td>+61 8 8000 4120</td></tr>
      <tr><th>Fax:</th><td>08 8000 4121</td></tr>
      <tr><th>Email:</th><td>hello@dentistryonmarlow.com.au</td></tr>
      <tr><th>Website:</th><td>www.dentistryonmarlow.com.au</td></tr>
    </table>
  </section>
  <p class="info-block social">Join us on Socialnet</p>

  <section class="info-block hours">
    <h2 class="heading">Opening Hours:</h2>
    <table class="hours-table">
      <tr><th>Monday - Friday</th><td>8:30am - 5:30pm</td></tr>
      <tr><th>Saturday</th><td>8:30am - 12:30pm</td></tr>
    </table>
  </section>
  <p class="info-block urgent">Urgent care appointments available each weekday.</p>
  <p class="info-block parking">Easy car parking available at the rear of the building.</p>
  <div class="map" role="img" aria-label="Street map showing the practice location and rear car parks"></div>

  <header class="brand">
    <p class="brand-name">Dentistry on Marlow</p>
    <p class="brand-tagline">Caring dentistry for all ages</p>
  </header>
  <div class="photo photo--exterior" role="img" aria-label="Photo of the practice building exterior with signage"></div>
  <div class="photo photo--reception" role="img" aria-label="Photo of a receptionist welcoming a patient with a cup of tea"></div>
  <div class="photo photo--smile" role="img" aria-label="Photo of a patient smiling into a hand mirror beside her dentist"></div>
</main>
</body>
</html>
```